Brochure for Upscale Painting and Contractor Services Company

We are a higher end interior and exterior painting contractor which also provides a range of other services as found on www.brindlecoatfinishes.net. Our edge in the market is being the "Gracious Painters" as we are clean shaven, kind to all customers, clean up more than we received it, timely with everything and do the best work around at the right price.

We need a brochure that reflects the elegance and quality of work we perform. We really want this to have a folder within to actually insert a letter and printed proposal from our founder so we can present on the spot or add flyers to and hand out at events, etc. We want something full page so no trifolds, rather a bifold with some means of have a folder insert.

The design should be elegant but bold with images.

Target Market(s)

We are typically working with women between 45-55 years of age living in homes worth $500K to $1m. You can imagine what they like (need) to see from contractors and we are already elegant and serving that need with our web and online communications but we need a print piece to match.

Industry/Entity Type

Painting

```html
<!DOCTYPE html>
<html lang="en">
<head>
<meta charset="utf-8">
<title>Brindlecoat Finishes – Folder Insert</title>
<link rel="stylesheet" href="https://fonts.googleapis.com/css2?family=Source+Sans+3:wght@300;400;600;700&family=Crimson+Text:wght@400;600;700&display=swap">
<style>
  :root{
    --canvas:#ffffff;
    --brand-red:#c3333a;
    --brand-red-dark:#a82a30;
    --band-grey:#5b5b5d;
    --ink:#3c3c3c;
    --accent:#c0392b;
    --star:#f5c400;
  }
  *{box-sizing:border-box;margin:0;padding:0}
  html,body{width:1200px;height:874px;overflow:hidden;background:var(--canvas)}
  body{position:relative;font-family:"Source Sans 3",Arial,sans-serif;color:var(--ink)}

  .page{position:absolute;top:0;width:594px;height:836px;overflow:hidden;
        background:linear-gradient(90deg,#f7f7f7 0%,#ffffff 45%,#f1f1f1 100%)}
  .page--front{left:0}
  .page--back{left:606px}

  .masthead{position:absolute;left:0;top:0;width:100%;height:100px;background:var(--brand-red)}
  .masthead__ribbon{position:absolute;left:0;top:0;width:100%;height:100px}
  .masthead__rule{position:absolute;left:0;top:100px;width:100%;height:13px;
        background:linear-gradient(180deg,#e2e2e2,#a8a8a8)}

  .footer__rule{position:absolute;left:0;top:780px;width:100%;height:21px;
        background:linear-gradient(90deg,#8f8f8f,#dcdcdc 35%,#dcdcdc 65%,#8f8f8f);
        text-align:center;font-size:13px;letter-spacing:3px;line-height:21px;color:#4a4a4a}
  .footer__band{position:absolute;left:0;top:804px;width:100%;height:32px;background:var(--brand-red)}

  .intro{position:absolute;left:40px;top:151px;width:518px;font-size:11px;line-height:14px;
         font-weight:300;color:#333;text-align:justify}
  .services-title{position:absolute;left:38px;top:208px;display:flex;align-items:center;gap:12px}
  .services-title__icon{width:56px;height:46px}
  .services-title h2{font-family:"Crimson Text",Georgia,serif;font-weight:600;font-size:20px;color:#2a2a2a}

  .service{position:absolute;width:133px;font-size:9.1px;line-height:11.7px;font-weight:300;
           color:#333;text-align:justify}
  .service h3{font-size:9.1px;font-weight:400;color:var(--accent)}
  .photo{position:absolute}

  .reviews-band{position:absolute;left:0;top:152px;width:100%;height:127px;background:var(--band-grey)}
  .reviews-band__headline{position:absolute;left:0;top:6px;width:100%;text-align:center;
           font-family:"Crimson Text",Georgia,serif;font-weight:700;font-size:14.5px;color:#fff}
  .listing{position:absolute;top:33px;width:113px;height:81px;background:#fff}
  .brand-card{position:absolute;left:335px;top:185px;width:182px;height:83px;background:#fff;
           border:4px solid var(--brand-red);display:flex;align-items:center;justify-content:center;
           gap:7px;font-family:"Crimson Text",Georgia,serif;font-weight:600;font-size:16px;color:var(--brand-red-dark)}
  .brand-card__mark{width:12px;height:12px;background:#222}
  .rating{position:absolute;left:344px;top:272px}
  .badge{position:absolute;left:472px;top:246px;width:40px;height:40px;border-radius:50%;background:var(--brand-red)}

  .why{position:absolute;width:242px;font-size:9.1px;line-height:11.8px;font-weight:300;
       color:#444;text-align:justify}
  .why h3{font-size:10.5px;font-weight:600;color:#333;margin-bottom:10px}
  .why p + p{margin-top:10px}

  .page-label{position:absolute;top:845px;width:594px;text-align:center;font-size:21px;
              font-weight:400;color:#e0313a}
</style>
</head>
<body>

<section class="page page--front">
  <header class="masthead">
    <svg class="masthead__ribbon" viewBox="0 0 594 100" preserveAspectRatio="none" role="img" aria-label="Sweeping rainbow ribbon artwork">
      <defs>
        <linearGradient id="ribbonFront" x1="0" x2="1" y1="0" y2="0">
          <stop offset="0" stop-color="#8fd13a"/>
          <stop offset="0.25" stop-color="#f6d11a"/>
          <stop offset="0.5" stop-color="#ef7d1a"/>
          <stop offset="0.75" stop-color="#d8278b"/>
          <stop offset="1" stop-color="#c3333a" stop-opacity="0"/>
        </linearGradient>
      </defs>
      <rect width="594" height="100" fill="url(#ribbonFront)" opacity="0.85"/>
    </svg>
  </header>
  <div class="masthead__rule"></div>

  <p class="intro">Though painting is our core expertise, we have extensive experience with many other aspects of the home improvement trade. Below is a list of some of the services we provide but please feel free to inquire within should you have a project that is not listed below. We will be happy to work with you to achieve your project goals.</p>

  <div class="services-title">
    <svg class="services-title__icon" viewBox="0 0 56 46" role="img" aria-label="Service bell picture"><ellipse cx="28" cy="26" rx="26" ry="18" fill="#6f6f6f"/></svg>
    <h2>Our Services</h2>
  </div>

  <article class="service" style="left:38px;top:273px">
    <h3>Painting</h3>
    Our high quality painting services do not simply provide the painting but also prepping, sanding, caulking, patching drywall holes and cracks, priming, fixing water damage, and much more. Prep prior to painting is the key to a great paint job. We also provide expert advice on the different qualities of various paint products. Beware of the lowest bidder for painting services. We may not always provide the lowest cost but we are the best and believe you get what you pay for in life.
  </article>
  <article class="service" style="left:38px;top:487px">
    <h3>Power Washing</h3>
    Whole house washing, freshen vinyl or aluminum siding, deep cleaning of all exterior surfaces. Great for decks prior to staining or sealing. Remove mold, mildew and grime.
  </article>
  <article class="service" style="left:38px;top:605px">
    <h3>Staining and Sealing</h3>
    We provide a superior process of prepping areas to be stained or sealed. There is no rushing a good quality job. We provide advice and guidance for high end product lines and the application of such products, including different polyurethanes as well as sealers for decks, whether they be natural/clear tones or with toners added (color).
  </article>

  <svg class="photo" style="left:177px;top:301px" width="118" height="77" role="img" aria-label="Photo of a painter rolling a wall"><rect width="118" height="77" fill="#a9d1c4"/></svg>
  <svg class="photo" style="left:177px;top:423px" width="118" height="57" role="img" aria-label="Photo of a worker power washing a brick home"><rect width="118" height="57" fill="#8a6f5a"/></svg>
  <svg class="photo" style="left:177px;top:520px" width="118" height="72" role="img" aria-label="Photo of a roller staining a wooden deck"><rect width="118" height="72" fill="#b58858"/></svg>

  <article class="service" style="left:307px;top:273px">
    <h3>Wallpaper Removal</h3>
    This is a job no one likes to do and most don't do it correctly. We remove wallpaper regularly and do so as environmentally friendly as possible and with no harmful chemicals. Our process involves simply removing the top layer of paper (what you see) then applying hot water to the backing several times, which will reactivate the paste and allow easier removal of that layer. We then wash down the walls and remove as much adhesive paste as possible. In the event that some paste is left on the walls the surface needs to be sealed out with an oil primer. Then as needed any marks and imperfections on the walls need to be skimmed out.
  </article>
  <article class="service" style="left:307px;top:533px">
    <h3>Gutter Cleaning</h3>
    Obviously gutters collect leaves and debris throughout the year, particularly during autumn. We can clean out and wipe down keeping an unobstructed flow of water out of your gutters. As oxidation discolors and fades the gutters over time, we can also give them a new look by painting them, providing a very affordable way to renew the look of your house and give it a crisp look.
  </article>
  <article class="service" style="left:307px;top:700px">
    <h3>Color Consulting</h3>
    Advising clients of ideal different color compliments for furniture match and decor match, thereby allowing smoother transitions from room to room.
  </article>

  <svg class="photo" style="left:447px;top:449px" width="118" height="73" role="img" aria-label="Photo of a painter working on a wall"><rect width="118" height="73" fill="#d9c8a8"/></svg>
  <svg class="photo" style="left:447px;top:564px" width="118" height="78" role="img" aria-label="Photo of hands clearing leaves from a gutter"><rect width="118" height="78" fill="#6f6a5e"/></svg>
  <svg class="photo" style="left:447px;top:685px" width="118" height="78" role="img" aria-label="Photo of a couple choosing from a colour fan deck"><rect width="118" height="78" fill="#c7a98a"/></svg>

  <div class="footer__rule">www.brindlecoatfinishes.net</div>
  <div class="footer__band"></div>
</section>

<section class="page page--back">
  <header class="masthead">
    <svg class="masthead__ribbon" viewBox="0 0 594 100" preserveAspectRatio="none" role="img" aria-label="Sweeping rainbow ribbon artwork">
      <defs>
        <linearGradient id="ribbonBack" x1="0" x2="1" y1="0" y2="0">
          <stop offset="0" stop-color="#1f9ad6"/>
          <stop offset="0.25" stop-color="#8fd13a"/>
          <stop offset="0.5" stop-color="#f6d11a"/>
          <stop offset="0.75" stop-color="#d8278b"/>
          <stop offset="1" stop-color="#c3333a" stop-opacity="0"/>
        </linearGradient>
      </defs>
      <rect width="594" height="100" fill="url(#ribbonBack)" opacity="0.85"/>
    </svg>
  </header>
  <div class="masthead__rule"></div>

  <div class="reviews-band">
    <p class="reviews-band__headline">we are the number one reviewed painting contractor locally on Findwell Reviews,</p>
    <div class="listing" style="left:56px" role="img" aria-label="Review site listing"></div>
    <div class="listing" style="left:194px" role="img" aria-label="Review site listing"></div>
  </div>
  <div class="brand-card"><span class="brand-card__mark"></span>Brindlecoat Finishes</div>
  <svg class="rating" width="96" height="17" viewBox="0 0 96 17" role="img" aria-label="Five star rating">
    <defs><polygon id="star" points="8,0 10.3,5.6 16,6 11.6,9.8 13,16 8,12.6 3,16 4.4,9.8 0,6 5.7,5.6"/></defs>
    <g fill="var(--star)">
      <use href="#star"/><use href="#star" x="20"/><use href="#star" x="40"/><use href="#star" x="60"/><use href="#star" x="80"/>
    </g>
  </svg>
  <div class="badge"></div>

  <div class="why" style="left:43px;top:308px">
    <p>With so many painting contractors to choose from, why would you choose us? First, if you ever worked with us before, you know why, but for those who have not, allow us to explain.</p>
  </div>
  <div class="why" style="left:43px;top:355px">
    <h3>The Gracious Painters</h3>
    <p>Most importantly, we are all gentlemen. We insist that every member of our team live up to a standard practically unknown to our industry.</p>
  </div>
  <div class="why" style="left:43px;top:428px">
    <h3>Honesty</h3>
    <p>We are honest and will remain transparent throughout all phases of your project.</p>
  </div>
  <div class="why" style="left:43px;top:489px">
    <h3>True Locals</h3>
    <p>We are local and have been serving Harborview and the surrounding area for more than 20 years. Our continued success in our home town means a lot to us and should to you as well. See our owner's bio here to learn more.</p>
  </div>
  <div class="why" style="left:43px;top:573px">
    <h3>Quality</h3>
    <p>We insist on very high standards for quality and will not consider a job complete until the client is completely satisfied. We encourage you to check out our objective reviews on Findwell and to ask for references, we will provide as many as you request.</p>
  </div>
  <div class="why" style="left:43px;top:658px">
    <h3>Pricing</h3>
    <p>We will not overcharge or coerce you into work that is not necessary or you do not want completed. We are not always the least expensive but always the best for the final product and experience you will have. We are worth every penny of what we charge. For more information on our pricing and what to consider when looking for a contractor, please check out our pricing page.</p>
  </div>

  <div class="why" style="left:305px;top:308px">
    <h3>Cleanliness</h3>
    <p>We are neat and will leave your place as we found it. Everytime.</p>
  </div>
  <div class="why" style="left:305px;top:357px">
    <h3>Efficient</h3>
    <p>We are efficient but will not rush.</p>
  </div>
  <div class="why" style="left:305px;top:405px">
    <h3>Expertise</h3>
    <p>We have experts with decades of experience for each service we provide, especially our painting services. We send the team member with the best skills for the needs of each project while understanding that no two projects are the same.</p>
  </div>
  <div class="why" style="left:305px;top:490px">
    <h3>Confidence</h3>
    <p>We sincerely believe we are the best painting contractor in Harborview and the surrounding area.</p>
    <p>We generally expect people to shop around so we believe it is essential to know who you are hiring and what to consider. Be sure to check out our pricing section to learn even more. Though we take our job very seriously we also like to enjoy a good, genuine relationship with our customers and our team. Check out the video below to get a sense of what it means to us to be the Gracious Painters.</p>
  </div>

  <div class="footer__rule">www.brindlecoatfinishes.net</div>
  <div class="footer__band"></div>
</section>

<p class="page-label" style="left:0">insert page 1 front</p>
<p class="page-label" style="left:606px">insert page 1 Back</p>

</body>
</html>
```